Supplement label for Brain health

I need a design for a supplement this supplement is a brain boost supplement.

The Name is Kelp Vantor.

I have attached other labels I like. This is for 50 plus demographic so the lettering needs to be easy to read and stand out. I have attached a dummy label template that once the winner is choosen then they will get the real supplement facts etc.

Clean desgin easy to read.

This file must be finished in AI format.

Target Market(s)

50 plus 70 percent female 30 percent male

Industry/Entity Type

Supplement

Font styles to use
Other font styles liked:
• Myrid pro maybe

Requirements
Must have
• easy to read text so no colors that hide text or hard to read.

```html
<!DOCTYPE html>
<html lang="en">
<head>
<meta charset="utf-8">
<title>Kelp Vantor – Supplement Label</title>
<link rel="stylesheet" href="https://fonts.googleapis.com/css2?family=Arimo:wght@400;700&family=Roboto+Condensed:wght@700&family=Russo+One&display=swap">
<style>
  :root {
    --page-bg: #eceeef;
    --label-bg-light: #eef2f4;
    --label-bg-mid: #d3dde2;
    --label-edge: #5d7fa8;
    --frame-orange: #d9772e;
    --ink: #111111;
    --ink-soft: #222222;
    --brain-light: #f4f7f8;
    --brain-mid: #aeb9bf;
    --brain-dark: #6f7c84;
  }
  * { box-sizing: border-box; margin: 0; padding: 0; }
  html, body { width: 1200px; height: 1200px; overflow: hidden; }
  body {
    background: var(--page-bg);
    font-family: "Arimo", Arial, sans-serif;
    color: var(--ink);
    position: relative;
  }
  .label {
    position: absolute;
    left: 10px; top: 380px;
    width: 1180px; height: 439px;
    border: 2px solid var(--label-edge);
    background:
      radial-gradient(ellipse at 50% 45%, var(--label-bg-light) 0%, var(--label-bg-mid) 70%, #c5d1d8 100%);
  }
  .label-frame {
    position: absolute;
    left: 10px; top: 10px; right: 10px; bottom: 10px;
    border: 1.5px solid var(--frame-orange);
  }

  /* Left column */
  .usage {
    position: absolute;
    left: 25px; top: 37px; width: 278px;
    font-size: 10.2px; line-height: 11.8px;
    text-align: justify;
    color: var(--ink-soft);
  }
  .usage p + p { margin-top: 11px; }
  .usage strong { font-weight: 700; }
  .fda-note {
    position: absolute;
    left: 26px; top: 300px; width: 234px; height: 37px;
    border: 1.5px solid var(--ink);
    padding: 2px 4px;
    font-size: 7.4px; line-height: 9.4px; font-weight: 700;
  }
  .distributor {
    position: absolute;
    left: 28px; top: 356px;
    font-family: "Roboto Condensed", "Arial Narrow", sans-serif;
    font-weight: 700;
    font-size: 13.5px; line-height: 17px;
  }

  /* Center column */
  .brand {
    position: absolute;
    left: 330px; top: 22px; width: 500px;
    text-align: center;
    font-family: "Russo One", Impact, sans-serif;
  }
  .brand-name {
    font-size: 56px; line-height: 64px;
    letter-spacing: 0.5px;
    transform: skewX(-10deg);
  }
  .brand-tagline {
    margin-top: 2px;
    font-size: 18px; letter-spacing: 0.6px;
    transform: skewX(-10deg);
  }
  .brain-art {
    position: absolute;
    left: 440px; top: 144px; width: 268px; height: 218px;
  }
  .net-count {
    position: absolute;
    left: 330px; top: 380px; width: 500px;
    text-align: center;
    font-family: "Russo One", Impact, sans-serif;
    font-size: 16.5px; letter-spacing: 0.3px;
    transform: skewX(-10deg);
  }

  /* Right column */
  .facts {
    position: absolute;
    left: 866px; top: 40px; width: 276px;
    border: 1.5px solid var(--ink);
    padding: 1px 5px 2px;
    font-size: 11px; line-height: 13px;
  }
  .facts-title {
    font-weight: 700; font-size: 25px; line-height: 28px;
    letter-spacing: 0.3px;
  }
  .facts-serving { padding-left: 2px; padding-bottom: 3px; border-bottom: 5px solid var(--ink); }
  .facts-head { font-size: 9px; line-height: 11px; letter-spacing: -0.4px; padding: 2px 2px; border-bottom: 2px solid var(--ink); }
  .facts-table { width: 100%; border-collapse: collapse; }
  .facts-table td { vertical-align: top; padding: 0; border-bottom: 1px solid #333; }
  .facts-table tr.no-rule td { border-bottom: none; }
  .facts-table .amt { text-align: right; width: 60px; padding-right: 14px; }
  .facts-table .dv { text-align: right; width: 8px; }
  .facts-table .sub { display: block; padding-left: 5px; }
  .facts-foot { padding-top: 1px; }
  .facts em { font-style: italic; }

  .other {
    position: absolute;
    left: 866px; top: 306px; width: 278px;
    font-size: 10.5px; line-height: 11.6px;
    text-align: justify;
  }
  .other strong { font-weight: 700; }
  .other .caps { font-weight: 700; }
  .other .gap { margin-top: 12px; }
</style>
</head>
<body>
  <section class="label" aria-label="Kelp Vantor supplement label">
    <div class="label-frame"></div>

    <div class="usage">
      <p><strong>SUGGESTED USE:</strong> 1 capsule taken 1 to 2 times daily preferably with meals or as directed by a healthcare professional.</p>
      <p><strong>CAUTION:</strong> Do not exceed recommended dose. St. John’s Wort may contribute to photosensitivity resulting in skin irritation and redness in persons exposed to strong sunlight or tanning booths. Avoid use in patients at risk of bleeding, taking anticoagulants, or with clotting disorders, based on case reports of bleeding. Discontinue use 2-3 weeks prior to some surgical and dental procedures due to increased risk of bleeding. Avoid use in couples who are trying to conceive, based on theoretical reduction of fertility. Pregnant or nursing mothers, children under 18, individuals with history of seizure, taking MAO inhibiting drugs, or with a known medical condition should consult a physician before using this or any dietary supplement. This product is manufactured and packaged in a facility which may also process milk, soy, wheat, egg, peanuts, tree nuts, fish and crustacean shellfish.</p>
    </div>

    <div class="fda-note">†These statements have not been evaluated by the Food &amp; Drug Administration. This product is not intended to diagnose, treat, cure or prevent any disease.</div>

    <div class="distributor">
      Distributed by:<br>Company Name<br>Full Address and Phone
    </div>

    <div class="brand">
      <div class="brand-name">Kelp Vantor</div>
      <div class="brand-tagline">CLARITY | FOCUS | MEMORY</div>
    </div>

    <svg class="brain-art" role="img" aria-label="Illustration of a silver human brain with a grid overlay" viewBox="0 0 268 218">
      <defs>
        <radialGradient id="brainTone" cx="50%" cy="40%" r="60%">
          <stop offset="0%" stop-color="var(--brain-light)"/>
          <stop offset="60%" stop-color="var(--brain-mid)"/>
          <stop offset="100%" stop-color="var(--brain-dark)"/>
        </radialGradient>
      </defs>
      <ellipse cx="134" cy="100" rx="132" ry="92" fill="url(#brainTone)" opacity="0.85"/>
    </svg>

    <div class="net-count">60 CAPSULES DIETARY SUPPLEMENT</div>

    <div class="facts">
      <div class="facts-title">Supplement Facts</div>
      <div class="facts-serving">Serving Size 1 Capsule<br>Servings Per Container: 30</div>
      <div class="facts-head">Amt Per Serv. &nbsp;&nbsp;%DV/RDI</div>
      <table class="facts-table">
        <tr><td><em>Ginkgo biloba</em> Leaf (24% extract)</td><td class="amt">50mg</td><td class="dv">*</td></tr>
        <tr class="no-rule"><td>Phosphatidylserine 4% Complex</td><td class="amt">125mg</td><td class="dv">*</td></tr>
        <tr><td colspan="3"><span class="sub">(consisting of Lecithin and Phosphatidylserine)</span></td></tr>
        <tr><td>N-Acetyl L-Carnitine HCl</td><td class="amt">50mg</td><td class="dv">*</td></tr>
        <tr><td>St. John’s Wort (0.3% extract)<span class="sub">(flower heads)</span></td><td class="amt">250mg</td><td class="dv">*</td></tr>
        <tr><td>L-Glutamine</td><td class="amt">150mg</td><td class="dv">*</td></tr>
        <tr><td><em>Bacopa monnieri</em> Leaf Extract<span class="sub">(20% bacosides)</span></td><td class="amt">120mg</td><td class="dv">*</td></tr>
        <tr><td>Vinpocetine (seeds)</td><td class="amt">2mg</td><td class="dv">*</td></tr>
        <tr><td>Huperzine-A (aerial plant)</td><td class="amt">10mcg</td><td class="dv">*</td></tr>
      </table>
      <div class="facts-foot">*Daily Value not established.</div>
    </div>

    <div class="other">
      <p><strong>Other ingredients:</strong> Gelatin (bovine), microcrystalline cellulose, vegetable magnesium stearate, and silicon dioxide.</p>
      <p class="caps">ALLERGEN WARNING: CONTAINS SOY (LECITHIN).</p>
      <p class="caps gap">KEEP OUT OF THE REACH OF CHILDREN.<br>DO NOT USE IF SAFETY SEAL IS DAMAGED OR MISSING. STORE IN A COOL, DRY PLACE.</p>
    </div>
  </section>
</body>
</html>
```